Webdesign für berufliches Schulzentrum für Ernährung, Gastgewerbe, Gesundheit
Zielgruppe
Berufliches Schulzentrum für Ernährung, Gastgewerbe, Gesundheit
Zielgruppe: Schüler und Auszubildende
Aufgabenstellung
- modernes, aber dennoch strukturiertes Aussehen der Webseite
- einfache Navigation
- die beiden Grüntöne aus dem Logo sollen sich bitte in der Seite wiederfinden - jedoch in freundlicher Form

```html
<!DOCTYPE html>
<html lang="de">
<head>
<meta charset="utf-8">
<title>Aktuelles – Schulzentrum Lindenau</title>
<link href="https://fonts.googleapis.com/css2?family=Montserrat:wght@600;700&family=Work+Sans:wght@300;400;500&display=swap" rel="stylesheet">
<style>
:root{
  --bg:#efefef;
  --page:#ffffff;
  --ink:#2b2b2b;
  --dark-green:#1f4a33;
  --mint:#c6ead0;
  --hero-a:#8fc5a4;
  --hero-b:#3f7a5c;
  --hero-c:#254d37;
}
*{margin:0;padding:0;box-sizing:border-box}
html,body{width:1200px;height:1200px;overflow:hidden;background:var(--bg)}
body{position:relative;font-family:"Work Sans",sans-serif;color:var(--ink)}
.page-label{position:absolute;left:150px;top:1168px;transform:rotate(-90deg);transform-origin:0 0;font:300 29px "Work Sans",sans-serif;color:#444;white-space:nowrap}
.page{position:absolute;left:212px;top:32px;width:776px;height:1136px;background:var(--page);box-shadow:0 2px 8px rgba(0,0,0,.25);overflow:hidden}
.site-header{position:absolute;left:0;top:0;width:100%;height:58px;background:#f3f3f3;display:flex;align-items:center}
.brand{position:absolute;left:14px;top:6px;width:86px;height:46px;display:flex;align-items:center;gap:5px}
.brand-mark{width:9px;height:9px;background:var(--dark-green);flex:none}
.brand-name{font:500 9px/1.15 "Work Sans",sans-serif;color:var(--dark-green)}
.main-nav{position:absolute;left:127px;top:0;height:58px;display:flex;align-items:center;gap:0}
.main-nav a{font:600 6.6px "Montserrat",sans-serif;letter-spacing:1.3px;color:#222;text-decoration:none;margin-right:17px;white-space:nowrap}
.main-nav a.active{text-decoration:underline;text-underline-offset:3px}
.menu-toggle{position:absolute;right:16px;top:22px;width:16px}
.menu-toggle span{display:block;height:1.3px;background:#222;margin-bottom:4.5px}
.hero{position:absolute;left:0;top:58px;width:100%;height:230px}
.hero-photo{position:absolute;inset:0;background:linear-gradient(100deg,var(--hero-a) 0%,var(--hero-b) 55%,var(--hero-c) 100%)}
.hero-kicker{position:absolute;top:46px;width:100%;text-align:center;color:#fff;font:500 11px "Work Sans",sans-serif;letter-spacing:1px}
.hero-title{position:absolute;width:100%;text-align:center;color:#fff;font:500 26px "Work Sans",sans-serif;letter-spacing:5px}
.hero-title span{display:inline-block;background:rgba(255,255,255,.22);padding:3px 14px}
.hero-title.one{top:67px}
.hero-title.two{top:111px}
.hero-btn{position:absolute;left:322px;top:171px;width:132px;height:31px;background:#fff;display:flex;align-items:center;justify-content:center;font:600 8.5px "Montserrat",sans-serif;letter-spacing:1.6px;color:#222}
.photo{position:absolute;width:302px;height:346px}
.photo-team{left:53px;top:305px;background:linear-gradient(160deg,#c8b98a 0%,#3d4b8a 35%,#3a3230 70%,#d9c9a6 100%)}
.photo-bread{left:424px;top:708px;background:linear-gradient(170deg,#e5d6c4 0%,#b06e36 45%,#d9a46a 75%,#efe2d0 100%)}
.arrow{position:absolute;width:25px;height:25px}
.dots{position:absolute;display:flex;gap:2px}
.dots i{width:6px;height:6px;border-radius:50%;border:1px solid var(--dark-green)}
.dots i.on{background:var(--dark-green)}
.post-title{position:absolute;font:400 21px/26px "Work Sans",sans-serif;letter-spacing:3px;color:#333}
.post-body{position:absolute;width:300px;font:400 8.9px/12.5px "Work Sans",sans-serif;letter-spacing:.7px;color:#222}
.post-body p+p{margin-top:12.5px}
.date-badge{position:absolute;height:21px;background:var(--mint);font:400 12px "Work Sans",sans-serif;letter-spacing:2.2px;color:#1b3a28;display:flex;align-items:center}
</style>
</head>
<body>
<div class="page-label">Aktuelles Seite</div>
<main class="page">
  <header class="site-header">
    <div class="brand"><span class="brand-mark"></span><span class="brand-name">Schulzentrum Lindenau</span></div>
    <nav class="main-nav">
      <a>ÜBER UNS</a><a>SCHULARTEN</a><a>PLÄNE/TERMINE</a><a class="active">AKTUELLES</a><a style="margin-right:11px">SCHULANMELDUNG</a><a style="margin-right:14px">IMPRESSION</a><a style="margin-right:14px">FÖRDERVEREIN</a><a>KONTAKT</a>
    </nav>
    <div class="menu-toggle"><span></span><span></span><span></span></div>
  </header>

  <section class="hero">
    <div class="hero-photo" role="img" aria-label="Foto einer lächelnden Schülerin mit Tasse, grün eingefärbt"></div>
    <p class="hero-kicker">Auf dem neusten Stand.</p>
    <h1 class="hero-title one"><span>UNSERE</span></h1>
    <h1 class="hero-title two"><span>AKTUELLEN BEITRÄGE</span></h1>
    <div class="hero-btn">Aktuelle Termine</div>
  </section>

  <article>
    <div class="photo photo-team" role="img" aria-label="Foto der Gewinner des Jugendwettbewerbs mit Pokalen und Urkunden"></div>
    <svg class="arrow" style="left:13px;top:463px" viewBox="0 0 25 25"><circle cx="12.5" cy="12.5" r="11.8" fill="none" stroke="#1b2b22" stroke-width="1.2"/><path d="M17 12.5H8M11 9.5l-3 3 3 3" fill="none" stroke="#1b2b22" stroke-width="1.1"/></svg>
    <svg class="arrow" style="left:363px;top:463px" viewBox="0 0 25 25"><circle cx="12.5" cy="12.5" r="11.8" fill="none" stroke="#1b2b22" stroke-width="1.2"/><path d="M8 12.5h9M14 9.5l3 3-3 3" fill="none" stroke="#1b2b22" stroke-width="1.1"/></svg>
    <div class="dots" style="left:188px;top:669px"><i class="on"></i><i></i><i></i><i></i><i></i></div>
    <h2 class="post-title" style="left:418px;top:320px">Rinderbäckchen<br>zwischen Bauernprotesten<br>und Bahnstreik</h2>
    <div class="post-body" style="left:418px;top:418px">
      <p>Am 9. und 10. Januar 2024 fand am Schulzentrum Lindenau der 32. Jugendwettbewerb in den gastronomischen Ausbildungsberufen statt. Insgesamt waren über 30 Azubis aus den Bereichen Hotel, Küche und Restaurant aus ganz Mittelsachsen am Start. Nach dem Vorentscheid, es galt in 60 Minuten möglichst viele Fragen aus der Fachtheorie via PC richtig zu beantworten und 20 typische Waren bzw. Geräte zu erkennen, erreichten 8 Köche und 8 Restaurant- bzw. Hotelfachleute die Endrunde.</p>
      <p>Während die Köche danach an ihrem Menü feilten, planten die anderen Starter die Veranstaltung für den 2. Wettbewerbstag: Wie wird die Aula eingerichtet, was kommt auf die Tafel, wer sitzt neben wem? In Teams – je ein Koch und eine Servicekraft – wurden dann Feinheiten besprochen und im Rahmen einer Weinschulung die passenden Tröpfchen zum Menü ausgewählt.</p>
    </div>
    <div class="date-badge" style="left:617px;top:665px;width:159px;padding-left:9px">September 2023</div>
  </article>

  <article>
    <h2 class="post-title" style="left:56px;top:728px">Einmal München und<br>zurück – Unser Besuch<br>der BAKA</h2>
    <div class="post-body" style="left:56px;top:825px">
      <p>Morgens früh 5.00 Uhr am 23.10.2023 starteten 65 Azubis des Fachbereiches Ernährung mit dem Bus in Lindenau um Messeluft zu schnuppern. Es ging auf die führende Weltmesse für Bäckerei, Konditorei und Snacks BAKA (Internationale Backmesse) nach München. Dort angekommen wurden die Auszubildenden von Jonas Berger, Referent für Berufsbildung und Fachkräftesicherung des Bundesverbandes des Bäckerhandwerks e. V., begrüßt und zu einem kleinen Rundgang in der Halle des Handwerks eingeladen. Danach konnte jeder entsprechend den eigenen Interessen die riesige Messe erkunden.</p>
      <p>Es gab viel zu entdecken. Man konnte den internationalen Teams von Bäckermeistern und Bäckermeisterinnen bei ihren Arbeiten zu den Deutschen Meisterschaften (World Bakers Cup 2023) live zu sehen und ihre perfekten Gebäcke und einzigartigen Schaustücke bestaunen. Im BAKA Start-up-Bereich wurden den Besuchern Innovationen präsentiert.</p>
    </div>
    <div class="date-badge" style="left:0;top:1068px;width:161px;padding-left:84px">Juli 2023</div>
    <div class="photo photo-bread" role="img" aria-label="Foto einer Brotauslage mit kunstvoll gebackenem Hirschkopf"></div>
    <svg class="arrow" style="left:388px;top:866px" viewBox="0 0 25 25"><circle cx="12.5" cy="12.5" r="11.8" fill="none" stroke="#1b2b22" stroke-width="1.2"/><path d="M17 12.5H8M11 9.5l-3 3 3 3" fill="none" stroke="#1b2b22" stroke-width="1.1"/></svg>
    <svg class="arrow" style="left:738px;top:866px" viewBox="0 0 25 25"><circle cx="12.5" cy="12.5" r="11.8" fill="none" stroke="#1b2b22" stroke-width="1.2"/><path d="M8 12.5h9M14 9.5l3 3-3 3" fill="none" stroke="#1b2b22" stroke-width="1.1"/></svg>
    <div class="dots" style="left:565px;top:1072px"><i class="on"></i><i></i><i></i><i></i><i></i></div>
  </article>
</main>
</body>
</html>
```